Etiketten-Design für Nano-Brauerei
Sehr zufrieden mit dem Ergebniss. Hat das Bedürfnis sehr gut interpretiert und sehr schnell umgesetzt. Reaktion immer innerhalb weniger Stunden.. Sehr gut weiter so... Gerne wieder,!
Zielgruppe
Wir sind eine nano brauerei im talquell Schweiz. Wir produzieren in kleinsten Mengen hochwertige Biere und agieren mehrheitlich in den nischenmärkte. Unsere Zielgruppe ist mehrheitlich männlich im mittleren Preissegment. Welche das Bierdrinken celebrieren. Zudem bieten wir Spezial iere an welche besonders Frauen ansprechen...
Aufgabenstellung
Das Bergpanorama.. Besonders die silhouette soll erkennbar sein. Die Etikette soll Farbe und Biersorte selber editierbar sein. Farbe und Text Beispiele im Excel.. Ibu und Farbe des Biers auf der Etikette ist nicht Pflicht. Text wie Pfand. Das Schloss kann dezent eingearbeitet sein. Mindestenshaltbarkei, Bereich für Strichcode muss vorgesehen sein. Heute kein Logo vorhanden.. Für ein einfaches zb. mit Hopfen wäre ich sehr dankbar... äuä Craft Beer

```html
<!DOCTYPE html>
<html lang="de">
<head>
<meta charset="utf-8">
<title>Pale Ale – Etikette</title>
<link href="https://fonts.googleapis.com/css2?family=Caveat+Brush&family=Cabin:wght@400&family=PT+Sans+Narrow:wght@400&display=swap" rel="stylesheet">
<style>
  :root {
    --page: #ffffff;
    --paper: #e5e1d4;
    --frame: #7e9d2f;
    --ale-green: #9bb060;
    --stone: #a38d7b;
    --stone-soft: rgba(163, 141, 123, 0.85);
    --stone-faint: rgba(163, 141, 123, 0.5);
    --ink-brown: #7a4632;
    --label-shadow: 0 20px 30px rgba(0, 0, 0, 0.28);
  }
  * { box-sizing: border-box; margin: 0; padding: 0; }
  html, body { width: 848px; height: 1200px; overflow: hidden; background: var(--page); }
  .sheet { position: relative; width: 848px; height: 1200px; }

  .label {
    position: absolute;
    background: var(--paper);
    box-shadow: var(--label-shadow);
  }
  .label--front { left: 62px; top: 105px; width: 468px; height: 467px; }
  .label--back { left: 420px; top: 608px; width: 346px; height: 346px; }

  .frame { position: absolute; border: 1px solid var(--frame); }
  .label--front .frame--outer { inset: 14px 22px 18px 20px; }
  .label--front .frame--inner { inset: 25px 33px 29px 29px; }
  .label--back .frame--outer { inset: 10px 17px 13px 14px; }
  .label--back .frame--inner { inset: 19px 25px 22px 21px; }

  .brand-mark {
    position: absolute; left: 245px; top: 51px; width: 145px; height: 145px;
    border: 1px solid var(--ink-brown); border-radius: 50%;
    display: flex; align-items: center; justify-content: center;
  }
  .brand-name {
    font-family: "Cabin", sans-serif; font-size: 17px; color: var(--stone);
    text-align: center; line-height: 1.2;
  }

  .mountains { position: absolute; }
  .label--front .mountains {
    left: 20px; top: 205px; width: 424px; height: 98px;
    background: radial-gradient(ellipse 50% 50% at 50% 50%, var(--stone-soft) 0%, rgba(163,141,123,0.35) 60%, rgba(163,141,123,0) 100%);
  }
  .label--back .mountains {
    left: 17px; top: 200px; width: 310px; height: 72px;
    background: radial-gradient(ellipse 50% 50% at 50% 50%, var(--stone-faint) 0%, rgba(163,141,123,0.2) 60%, rgba(163,141,123,0) 100%);
  }

  .beer-style {
    position: absolute; left: 0; right: 0; text-align: center;
    font-family: "Caveat Brush", cursive; font-weight: 400; color: var(--ale-green);
    line-height: 1;
  }
  .label--front .beer-style {
    top: 318px; padding-left: 14px; font-size: 64px;
    letter-spacing: 0.12em; word-spacing: 0.2em;
  }
  .label--back .beer-style {
    top: 52px; font-size: 36px; letter-spacing: 0.1em; word-spacing: 0.15em;
  }

  .beer-stats {
    position: absolute; top: 95px; left: 91px; right: 97px;
    display: flex; justify-content: space-between;
    font-family: "Cabin", sans-serif; font-size: 13px; color: var(--stone);
  }

  .beer-description {
    position: absolute; top: 127px; left: 30px; right: 30px; text-align: center;
    font-family: "PT Sans Narrow", sans-serif; font-size: 7.8px; line-height: 12.2px;
    color: var(--ink-brown);
  }

  .brewery-contact {
    position: absolute; top: 256px; left: 0; right: 0; text-align: center;
    font-family: "Cabin", sans-serif; font-size: 13px; line-height: 17px;
    color: var(--stone); letter-spacing: 0.04em;
  }
</style>
</head>
<body>
<main class="sheet">
  <section class="label label--front">
    <div class="frame frame--outer"></div>
    <div class="frame frame--inner"></div>
    <div class="brand-mark">
      <p class="brand-name">talquell<br>craft beer</p>
    </div>
    <div class="mountains" role="img" aria-label="Bergpanorama-Silhouette in Braun"></div>
    <h1 class="beer-style">PALE ALE</h1>
  </section>

  <section class="label label--back">
    <div class="frame frame--outer"></div>
    <div class="frame frame--inner"></div>
    <h2 class="beer-style">PALE ALE</h2>
    <div class="beer-stats"><span>5.3% alc.</span><span>IBU 26</span></div>
    <p class="beer-description">
      Eine auf der ganzen Welt geliebte und weit verbreitete englische Biersorte.<br>
      Helle Farbe mit schöner Schaumkrone und ausgezeichnetem Hopfenbouquet<br>
      durch die Verwendung edler Hopfensorten und verschiedener Malze.<br>
      Leicht und süffig.
    </p>
    <div class="mountains" role="img" aria-label="Blasse Bergpanorama-Silhouette"></div>
    <p class="brewery-contact">
      Brauerei Talquell<br>
      Adresse 1 . 3245 Ort<br>
      www.brauereitalquell.com
    </p>
  </section>
</main>
</body>
</html>
```